Postcard Design

I need a postcard printed in black and white on one side only, with the name, address and a small logo in the shape of a beehive written straight along the top on one side.

I have a photo which I can send you of the logo

The wording is as follows......

Mira Pellow, The Larkspur, 14 Orchard Mews, London NW7 4QT.
T: 020 7461 3820 M: 07923481607 E: mira@mirapellow.example
www.mirapellow.example.

I would like the little beehive logo to go in the centre of the top line

Assuming the design is fine - it is not very difficult, please print 200 cards.

Target Market(s)

This is for private and business use

Font styles to use
Serif

Requirements
Must have
• Please choose a very classic font like book antica or Times new Roman. Can you choose a crisp and good quality white matt card for this.

```html
<!DOCTYPE html>
<html lang="en">
<head>
<meta charset="utf-8">
<title>Mira Pellow – Postcard</title>
<link rel="stylesheet" href="https://fonts.googleapis.com/css2?family=Sorts+Mill+Goudy&display=swap">
<style>
  :root {
    --ink: #1a1a1a;
    --tone-light: #ececec;
    --tone-mid: #d6d6d6;
    --paper: #ffffff;
  }
  html, body {
    margin: 0;
    padding: 0;
    width: 1200px;
    height: 849px;
    overflow: hidden;
    background: var(--paper);
  }
  .postcard {
    position: relative;
    width: 1200px;
    height: 849px;
    background: var(--paper);
  }
  .postcard__frame {
    position: absolute;
    left: 59px;
    top: 51px;
    width: 1076px;
    height: 739px;
    border: 3px solid var(--ink);
  }
  .postcard__emblem {
    position: absolute;
    left: 452px;
    top: 95px;
    width: 296px;
    height: 262px;
    background: linear-gradient(180deg, var(--tone-light) 0%, var(--tone-mid) 100%);
  }
  .postcard__details {
    position: absolute;
    left: 0;
    top: 371px;
    width: 1200px;
    margin: 0;
    text-align: center;
    font-family: "Sorts Mill Goudy", "Times New Roman", serif;
    font-size: 25.8px;
    line-height: 34px;
    font-variant-numeric: lining-nums;
    font-feature-settings: "lnum" 1;
    color: var(--ink);
    font-style: normal;
  }
  .postcard__line { display: block; white-space: pre; }
</style>
</head>
<body>
  <main class="postcard">
    <div class="postcard__frame"></div>
    <div class="postcard__emblem" role="img" aria-label="Small engraved emblem of a straw beehive on a bench among flowers"></div>
    <address class="postcard__details">
      <span class="postcard__line">Mira Pellow, The Larkspur, 14 Orchard Mews, London NW7 4QT.</span>
      <span class="postcard__line">T: 020 7461 3820  M: 07923481607  E: mira@mirapellow.example</span>
      <span class="postcard__line">www.mirapellow.example.</span>
    </address>
  </main>
</body>
</html>
```